Vesk Architecture

We are a architectural design and build company working between scales 1/1000 to 1/1 we want people to understand our difference from our design experience and quality.we build hotels restourants and office spaces.Our company name is Vesk architecture to mind sustainability.

We want to write our adress phone and work spesifications on the card and we want our logo as backround.

Ps:you could find the logo adress and phone box numbers from the web:www.veskmimarlik-ornek.com

Target Market(s)

Who looks for experts.

Industry/Entity Type

Architecture

Requirements
Must have
• Design is over everything.
Should not have
• we don want it to be colorfull

```html
<!DOCTYPE html>
<html lang="tr">
<head>
<meta charset="utf-8">
<title>Vesk Mimarlik – Business Card</title>
<link rel="stylesheet" href="https://fonts.googleapis.com/css2?family=Cormorant+Garamond:ital,wght@1,500&family=Montserrat:wght@400&family=Arimo:wght@400;700&display=swap">
<style>
  :root {
    --stage: #c9c9c9;
    --card: #fbfbfb;
    --card-stripe: #f1f1f1;
    --card-back: #e6e6e6;
    --ink: #141414;
    --ink-soft: #8d8d8d;
    --teal: #2e8479;
    --label: #3aa59a;
    --arc-light: #e4e4e4;
    --arc-mid: #c4c4c4;
    --arc-dark: #a8a8a8;
  }
  * { box-sizing: border-box; margin: 0; padding: 0; }
  html, body { width: 1200px; height: 900px; overflow: hidden; }
  body {
    background: var(--stage);
    display: flex;
    flex-direction: column;
    align-items: center;
    justify-content: center;
    gap: 50px;
    font-family: "Arimo", Arial, sans-serif;
  }
  .card {
    position: relative;
    width: 580px;
    height: 320px;
    overflow: hidden;
    box-shadow: 0 4px 14px rgba(0,0,0,.25);
  }
  .card--front {
    background: repeating-linear-gradient(to bottom, var(--card) 0 26px, var(--card-stripe) 26px 34px);
  }
  .card--back { background: var(--card-back); }
  .arc-band {
    position: absolute;
    left: 0; right: 0; bottom: 0;
    height: 96px;
    background: linear-gradient(to bottom, var(--arc-light), var(--arc-mid) 60%, var(--arc-dark));
  }
  .back-pattern {
    position: absolute;
    inset: 0;
    background: radial-gradient(ellipse at center, #eeeeee 0%, #dcdcdc 70%, #d2d2d2 100%);
  }
  .holder {
    position: absolute;
    left: 58px; top: 14px;
  }
  .holder__name {
    font-family: "Cormorant Garamond", Georgia, serif;
    font-style: italic;
    font-weight: 500;
    font-size: 27px;
    color: var(--teal);
    letter-spacing: 1px;
  }
  .holder__title {
    font-size: 14px;
    color: var(--ink);
    margin-left: 70px;
    margin-top: -2px;
  }
  .wordmark {
    position: absolute;
    left: 0; right: 0;
    text-align: center;
    font-family: "Montserrat", Arial, sans-serif;
    font-weight: 400;
    color: var(--ink);
  }
  .card--front .wordmark { top: 86px; }
  .card--back .wordmark { top: 90px; color: var(--ink-soft); }
  .wordmark__name { font-size: 86px; line-height: 1; letter-spacing: 2px; }
  .wordmark__sub { font-size: 22px; letter-spacing: 3px; margin-top: 4px; }
  .contact {
    position: absolute;
    right: 16px; bottom: 10px;
    font-size: 10.5px;
    font-weight: 700;
    line-height: 1.38;
    color: var(--ink);
  }
  .contact__label { color: var(--label); }
</style>
</head>
<body>
  <section class="card card--front" aria-label="Card front">
    <div class="arc-band" role="img" aria-label="Layered grey arc pattern along the bottom edge"></div>
    <div class="holder">
      <p class="holder__name">Deniz Arda KAYA</p>
      <p class="holder__title">Mimar</p>
    </div>
    <div class="wordmark">
      <p class="wordmark__name">vesk</p>
      <p class="wordmark__sub">MİMARLIK</p>
    </div>
    <address class="contact">
      Bahariye Mah. Lale Cad. Ilgin Sok.<br>
      No: 7 Yeldegirmeni/Istanbul<br>
      <span class="contact__label">Tel:</span> 0216 555 01 01<br>
      <span class="contact__label">F:</span> 0216 555 01 02<br>
      <span class="contact__label">E-mail:</span> info@veskmimarlik-ornek.com
    </address>
  </section>

  <section class="card card--back" aria-label="Card back">
    <div class="back-pattern" role="img" aria-label="Faint repeating grey arc pattern covering the card"></div>
    <div class="wordmark">
      <p class="wordmark__name">vesk</p>
      <p class="wordmark__sub">MİMARLIK</p>
    </div>
  </section>
</body>
</html>
```